Verpackungsdesign für Tajine
Zielgruppe
Wir sind ein produzierendes Unternehmen im grünen Herzen Deutschlands. Unser Fachgebiet ist die Fertigung von flammfester- und Gebrauchskeramik.
Nachhaltige Produkte, Made in Germany. Qualität, Kundenzufriedenheit und Nachhaltigkeit.
Aufgabenstellung
Die Verpackung ist für eine Tajine. Das Design ist für zwei unterschiedliche Verpackungsgrößen. Maße der Verpackung sind wie folgt: H27,5 x B30 x T30 cm und H30 x B36,5 x T36,5 cm. Das Design wird entweder direkt auf die Kartonage gedruckt oder als Folie von oben über den Karton gesteckt. Es sollte jede Seite, außer der Boden, bedruckt sein.
Die Kartonage ist für unsere gesamte Farbpalette (Tajine) gedacht, also sollte die Tajine in keiner bestimmten Farbe abgebildet werden (Vielleicht nur die Umrisse oder als Grafik, bloß als Beispiel). Gut wäre, wenn eine bestimmte stelle vorgesehen wird, auf der von uns ein kleiner Aufkleber angebracht werden kann. Der Aufkleber zeigt dann die Farbe und eventuell noch einen Barcode.
Das Design sollte die Produktdaten, die in der hochgeladenen PDF stehen, enthalten. Die Technischen Daten könnte ich mir auch gut als kleine Symbole vorstellen.
Es sind erstmal einige einfache Bilder anbei. Falls hier noch weitere Bilder oder bestimmte Vorstellungen gewünscht sind, dann können diese binnen 1-2 Tagen umgesetzt werden und zur Verfügung gestellt werden.

```html
<!DOCTYPE html>
<html lang="de">
<head>
<meta charset="utf-8">
<title>Hainberg Keramik – Tajine Verpackung</title>
<link rel="stylesheet" href="https://fonts.googleapis.com/css2?family=Montserrat:wght@400;600;700&display=swap">
<style>
  :root {
    --page: #d2d3d5;
    --board: #ffffff;
    --dark: #323233;
    --gold: #b6a640;
    --gold-light: #cdbd55;
    --text-gold: #cbb84a;
    --text-on-gold: #3a3a36;
    --cut: #e0442e;
  }
  * { margin: 0; padding: 0; box-sizing: border-box; }
  html, body { width: 1200px; height: 857px; overflow: hidden; background: var(--page); }
  .canvas { position: relative; width: 1200px; height: 857px; font-family: "Montserrat", sans-serif; color: var(--text-gold); }
  .dieline { position: absolute; left: 0; top: 0; }
  .copy { position: absolute; font-size: 5.1px; line-height: 9.3px; font-weight: 600; }
  .copy h3 { font-size: 6.6px; font-weight: 700; line-height: 9px; margin-bottom: 1px; }
  .copy ul { list-style: none; }
  .copy li { position: relative; padding-left: 5px; }
  .copy li::before { content: "•"; position: absolute; left: 0; }
  .contact { position: absolute; display: flex; align-items: center; gap: 6px; font-size: 5.6px; font-weight: 600; white-space: nowrap; }
  .contact svg { width: 9px; height: 9px; }
  .contact--on-gold { color: var(--text-on-gold); }
  .brand { position: absolute; display: flex; align-items: center; gap: 12px; font-weight: 400; color: var(--text-gold); white-space: nowrap; }
  .brand .mark { border: 1.2px solid var(--text-gold); }
  .brand--front { left: 621px; top: 411px; font-size: 18.5px; }
  .brand--front .mark { width: 32px; height: 30px; }
  .brand--lid { left: 95px; top: 285px; font-size: 16.5px; transform: rotate(180deg); }
  .brand--lid .mark { width: 31px; height: 30px; }
  .color-label { position: absolute; left: 866px; top: 565px; font-size: 6.8px; font-weight: 700; }
  .color-sticker { position: absolute; left: 894px; top: 565px; width: 46px; height: 21px; background: var(--board); }
</style>
</head>
<body>
<div class="canvas">
  <svg class="dieline" width="1200" height="857" viewBox="0 0 1200 857">
    <defs>
      <linearGradient id="photo-pair" x1="0" y1="0" x2="1" y2="0">
        <stop offset="0" stop-color="#3e48b8"/>
        <stop offset="0.3" stop-color="#5a62b4"/>
        <stop offset="0.7" stop-color="#c4bfb0"/>
        <stop offset="1" stop-color="#d2ccbc"/>
      </linearGradient>
      <linearGradient id="photo-pair-rev" x1="0" y1="0" x2="1" y2="0">
        <stop offset="0" stop-color="#cfc9b9"/>
        <stop offset="0.35" stop-color="#beb8a8"/>
        <stop offset="0.7" stop-color="#5a62b4"/>
        <stop offset="1" stop-color="#3e48b8"/>
      </linearGradient>
      <radialGradient id="blue-plate" cx="0.5" cy="0.5" r="0.5">
        <stop offset="0" stop-color="#2a34a6"/>
        <stop offset="1" stop-color="#4a52c2"/>
      </radialGradient>
      <radialGradient id="cream-lid" cx="0.5" cy="0.5" r="0.5">
        <stop offset="0" stop-color="#9a9486"/>
        <stop offset="1" stop-color="#c9c3b3"/>
      </radialGradient>
      <clipPath id="clip-col2"><rect x="325" y="363" width="262" height="239"/></clipPath>
      <clipPath id="clip-col4"><rect x="848" y="363" width="262" height="239"/></clipPath>
    </defs>

    <g class="flaps" fill="var(--board)" stroke="var(--cut)" stroke-width="0.8">
      <path d="M64,101 L64,98 Q64,71 91,71 L298,71 Q325,71 325,98 L325,101 Z"/>
      <path d="M325,363 L346,232 L566,232 L587,363 Z"/>
      <path d="M848,363 L869,232 L1089,232 L1110,363 Z"/>
      <path d="M1110,363 L1136,373 L1136,592 L1110,602 Z"/>
      <path d="M64,602 L64,772 Q64,785 77,785 L104,785 Q117,785 117,772 L117,733 L273,733 L273,772 Q273,785 286,785 L312,785 Q325,785 325,772 L325,602 Z"/>
      <path d="M325,602 L462,657 Q470,664 465,672 L458,686 Q455,698 470,698 L587,698 L587,602 Z"/>
      <path d="M587,602 L631,743 L631,772 Q631,785 644,785 L791,785 Q804,785 804,772 L804,743 L848,602 Z"/>
      <path d="M1110,602 L973,657 Q966,664 970,672 L977,686 Q980,698 965,698 L848,698 L848,602 Z"/>
      <path d="M177,101 L179,98 L209,98 L211,101" fill="none"/>
    </g>

    <g class="lid-panel">
      <rect x="64" y="101" width="261" height="262" fill="var(--gold)"/>
      <path d="M64,196 C120,158 210,150 325,160 L325,168 C220,160 130,170 64,206 Z" fill="var(--gold-light)"/>
      <path d="M64,206 C130,170 220,160 325,168 L325,363 L64,363 Z" fill="var(--dark)"/>
      <rect x="70" y="108" width="156" height="118" rx="44" fill="url(#photo-pair)" role="img" aria-label="Foto: zwei Tajine-Deckel in Blau und Creme"/>
    </g>

    <g class="side-panels">
      <rect x="64" y="363" width="1046" height="239" fill="var(--dark)"/>
      <path d="M420,602 C455,548 530,542 600,537 C700,530 790,525 848,508 L848,602 Z" fill="var(--gold)"/>
      <path d="M760,528 C800,522 830,512 848,500 L848,508 C820,520 790,526 760,530 Z" fill="var(--gold-light)"/>
      <circle cx="377" cy="555" r="56" fill="url(#blue-plate)" clip-path="url(#clip-col2)" role="img" aria-label="Foto: blaue Tajine von oben"/>
      <rect x="686" y="478" width="156" height="120" rx="46" fill="url(#photo-pair-rev)" role="img" aria-label="Foto: Tajine in Creme und Blau"/>
      <circle cx="1076" cy="562" r="62" fill="url(#cream-lid)" clip-path="url(#clip-col4)" role="img" aria-label="Foto: cremefarbener Tajine-Deckel von oben"/>
    </g>

    <g class="fold-lines" fill="none" stroke="var(--cut)" stroke-width="0.8">
      <rect x="64" y="363" width="1046" height="239"/>
      <line x1="64" y1="101" x2="64" y2="363"/>
      <line x1="325" y1="101" x2="325" y2="363"/>
      <line x1="64" y1="101" x2="325" y2="101"/>
      <line x1="325" y1="363" x2="325" y2="602"/>
      <line x1="587" y1="363" x2="587" y2="602"/>
      <line x1="848" y1="363" x2="848" y2="602"/>
    </g>

    <g class="tuck-tab">
      <path d="M700,363 L700,336 Q700,328 708,328 L727,328 Q735,328 735,336 L735,363 Z" fill="var(--dark)" stroke="var(--cut)" stroke-width="0.8"/>
      <path d="M700,363 L700,397 M735,363 L735,397" stroke="var(--cut)" stroke-width="0.8"/>
    </g>
  </svg>

  <div class="brand brand--lid"><span class="mark"></span><span>Hainberg Keramik</span></div>
  <div class="brand brand--front"><span class="mark"></span><span>Hainberg Keramik</span></div>

  <div class="copy" style="left:82px; top:378px; width:205px;">
    <h3>Hainberg Keramik</h3>
    <p>Unsere Firmengeschichte beginnt auf dem ehemaligen Firmengelände der zu DDR Zeiten größten Freihandtöpferei Europas, wo sich der Töpferhof Lindner in guter Nachbarschaft mit uns befindet. Keramik und Hainberg gehören seit über 500 Jahren zusammen und an dieser Tradition wollen wir festhalten.</p>
  </div>
  <div class="copy" style="left:82px; top:452px; width:205px;">
    <h3>Qualität</h3>
    <p>In einer der ehemaligen Produktionshallen ist mit viel Liebe und Arbeit ein neuer Betrieb entstanden. Mit unserem Keramikmeister K. Albers wollen wir neue Maßstäbe am Markt setzen und unseren Kunden stets die beste Qualität bieten. Unser Qualitätsanspruch hört nicht bei den Produkten auf, sondern erstreckt sich auf all unsere Prozesse wie beispielsweise Versand oder die schnelle Beantwortung von Kontaktanfragen.</p>
  </div>
  <div class="copy" style="left:82px; top:539px; width:120px; line-height:7.4px;">
    <h3>Firmendaten:</h3>
    <p style="margin-top:3px;">Hainberg Keramik GmbH,<br>Lindenweg 8,<br>98646 Hainberg, DE</p>
    <p style="margin-top:7px;">info@hainberg-keramik.de</p>
  </div>

  <div class="contact" style="left:217px; top:565px;">
    <svg viewBox="0 0 10 10" fill="none" stroke="currentColor" stroke-width="1"><circle cx="5" cy="5" r="4.3"/><ellipse cx="5" cy="5" rx="1.8" ry="4.3"/><line x1="0.7" y1="5" x2="9.3" y2="5"/></svg>
    <span>www.hainberg-keramik.de</span>
  </div>
  <div class="contact" style="left:217px; top:580px;">
    <svg viewBox="0 0 10 10" fill="none" stroke="currentColor" stroke-width="1"><rect x="0.8" y="0.8" width="8.4" height="8.4" rx="2"/></svg>
    <span>@hainbergkeramik</span>
  </div>

  <div class="copy" style="left:346px; top:378px; width:190px;">
    <h3>Technische Daten:</h3>
    <ul>
      <li>Material: Keramik (Steinzeug)</li>
      <li>Tajine Maße: 250x250x220 mm (kleines Verpackungsdesign) / Tajine Maße: 305x305x255 mm (großes Verpackungsdesign)</li>
      <li>Gewicht: 2,35 kg (kleines Verpackungsdesign) / Gewicht: 3,26kg (großes Verpackungsdesign)</li>
      <li>Fassungsvermögen: 1l (kleines Verpackungsdesign) / Fassungsvermögen: 2,3l (großes Verpackungsdesign)</li>
      <li>Spülmaschinen/Mikrowellengeeignet</li>
      <li>Einsetzbar auf Gas-, Glaskeramik-, Halogen-, Elektro-, Induktionsherdplatten (mit Adapterplatte), Ofen und Grill</li>
    </ul>
  </div>

  <div class="contact contact--on-gold" style="left:452px; top:565px;">
    <svg viewBox="0 0 10 10" fill="none" stroke="currentColor" stroke-width="1"><circle cx="5" cy="5" r="4.3"/><ellipse cx="5" cy="5" rx="1.8" ry="4.3"/><line x1="0.7" y1="5" x2="9.3" y2="5"/></svg>
    <span>www.hainberg-keramik.de</span>
  </div>
  <div class="contact contact--on-gold" style="left:452px; top:580px;">
    <svg viewBox="0 0 10 10" fill="none" stroke="currentColor" stroke-width="1"><rect x="0.8" y="0.8" width="8.4" height="8.4" rx="2"/></svg>
    <span>@hainbergkeramik</span>
  </div>

  <div class="copy" style="left:866px; top:378px; width:134px;">
    <h3>Zusatzinfos:</h3>
    <p>Wusstest du, dass Zutaten auf bestimmte Art und Weise in der Tajine platziert werden?</p>
  </div>
  <div class="copy" style="left:866px; top:421px; width:134px;">
    <h3>Die Regel ist:</h3>
    <p>Zutaten mit der längsten Garzeit gehören in die Mitte. Zutaten mit kürzeren Garzeiten werden an den Rand gelegt. Damit Fisch oder Fleisch nicht am Boden anbrennen, werden sie auf eine Schicht Gemüse gebettet.</p>
  </div>

  <div class="color-label">Farbe:</div>
  <div class="color-sticker"></div>
</div>
</body>
</html>
```